Ned Halvorsen Executive Coach Business Card Design

I need a new card design for my Executive Coaching practice. I am a Clinical Psychotherapist and Executive Coach. I help my clients get the most out of life by developing their personal and professional skills and abilities.

I work with senior executives. My design needs to be high end. I am thinking gloss on the front. I am also thinking contemporary. I am going to use a black, grey and red colour scheme on the the website. I am thinking grey with black and red accents. I would also like a water mark included on the card.

Target Market(s)

Senior Executives In major Companies

Industry/Entity Type

Business

Contact Information for Business Card

On the front

Ned Halvorsen
Clinical Psychotherapist and Executive Coach
For Personal and Professional Success

On the Back

Tarrant office
87 Tarrant Vale Road Tarrant

North Sydney Office
Suite 309 / 41 Pellow Street North Sydney

Danforth Street Office
Suite 512 / 248 Danforth Street Sydney CBD

Phone 02 95517384
Email ned@nedhalvorsen.example.au

Requirements
Must have
• Friendly but professional
Water Mark
Gloss Front

```html
<!DOCTYPE html>
<html lang="en">
<head>
<meta charset="utf-8">
<title>Ned Halvorsen – Business Card</title>
<link rel="stylesheet" href="https://fonts.googleapis.com/css2?family=Bebas+Neue&family=Open+Sans:wght@400;600&display=swap">
<style>
  :root {
    --backdrop: #c8c8c8;
    --card: #efefed;
    --ink: #111111;
    --accent-red: #c41e2e;
    --rule: #6a6a6a;
    --watermark: rgba(17, 17, 17, 0.05);
  }
  * { box-sizing: border-box; margin: 0; padding: 0; }
  html, body {
    width: 1200px;
    height: 856px;
    overflow: hidden;
    background: var(--backdrop);
  }
  .stage {
    width: 1200px;
    height: 856px;
    display: flex;
    align-items: center;
    justify-content: center;
  }
  .business-card {
    position: relative;
    width: 477px;
    height: 780px;
    background: var(--card);
    box-shadow: 0 4px 14px rgba(0,0,0,0.18);
    overflow: hidden;
  }
  .watermark {
    position: absolute;
    right: -6px;
    bottom: 52px;
    font-family: "Bebas Neue", "Oswald", sans-serif;
    font-size: 150px;
    line-height: 1;
    color: var(--watermark);
    letter-spacing: 2px;
    white-space: nowrap;
    z-index: 0;
    pointer-events: none;
  }
  .holder-name {
    position: absolute;
    left: 38px;
    top: 40px;
    font-family: "Bebas Neue", "Oswald", sans-serif;
    font-weight: 400;
    font-size: 106px;
    line-height: 0.9;
    color: var(--ink);
    letter-spacing: 1px;
    z-index: 1;
  }
  .rule {
    position: absolute;
    left: 46px;
    right: 34px;
    height: 1.5px;
    background: var(--rule);
    z-index: 1;
  }
  .rule-top { top: 236px; }
  .rule-mid { top: 486px; }
  .rule-bottom { top: 730px; background: var(--ink); }
  .profession {
    position: absolute;
    left: 44px;
    top: 252px;
    font-family: "Bebas Neue", "Oswald", sans-serif;
    font-weight: 400;
    font-size: 66px;
    line-height: 0.95;
    color: var(--accent-red);
    letter-spacing: 0.5px;
    z-index: 1;
  }
  .tagline {
    position: absolute;
    left: 46px;
    top: 452px;
    font-family: "Open Sans", "Segoe UI", sans-serif;
    font-weight: 600;
    font-size: 12.5px;
    letter-spacing: 2.2px;
    text-transform: uppercase;
    color: var(--ink);
    z-index: 1;
  }
  .contact-list {
    position: absolute;
    left: 50px;
    right: 24px;
    top: 512px;
    list-style: none;
    font-family: "Open Sans", "Segoe UI", sans-serif;
    font-size: 13px;
    line-height: 1.65;
    color: var(--ink);
    z-index: 1;
  }
  .contact-item {
    display: flex;
    align-items: flex-start;
    gap: 16px;
    margin-bottom: 22px;
  }
  .contact-icon {
    flex: none;
    width: 30px;
    height: 30px;
  }
  .contact-text { padding-top: 4px; }
</style>
</head>
<body>
<main class="stage">
  <article class="business-card">
    <div class="watermark" aria-hidden="true">Halvorsen</div>

    <h1 class="holder-name">Ned<br>Halvorsen</h1>
    <div class="rule rule-top"></div>
    <h2 class="profession">Clinical<br>Psychotherapist<br>&amp; Executive Coach</h2>
    <p class="tagline">For Personal and Professional Success</p>
    <div class="rule rule-mid"></div>

    <ul class="contact-list">
      <li class="contact-item">
        <svg class="contact-icon" viewBox="0 0 30 30" aria-hidden="true">
          <circle cx="15" cy="15" r="14" fill="var(--ink)"/>
          <path d="M7 15 L15 8 L23 15 L20.5 15 L20.5 22 L17 22 L17 18 L13 18 L13 22 L9.5 22 L9.5 15 Z" fill="var(--card)"/>
        </svg>
        <p class="contact-text">
          Tarrant: 87, Tarrant Vale Road, Tarrant.<br>
          North Sydney: 309 / 41, Pellow St, North Sydney.<br>
          Danforth St: 512 / 248, Danforth St, Sydney.
        </p>
      </li>
      <li class="contact-item">
        <svg class="contact-icon" viewBox="0 0 30 30" aria-hidden="true">
          <circle cx="15" cy="15" r="13.5" fill="none" stroke="var(--ink)" stroke-width="1.6"/>
          <rect x="10.5" y="7.5" width="9" height="15" rx="1.5" fill="none" stroke="var(--ink)" stroke-width="1.5"/>
          <line x1="13.5" y1="19.8" x2="16.5" y2="19.8" stroke="var(--ink)" stroke-width="1.2"/>
        </svg>
        <p class="contact-text">02 95517384</p>
      </li>
      <li class="contact-item">
        <svg class="contact-icon" viewBox="0 0 30 30" aria-hidden="true">
          <circle cx="15" cy="15" r="14" fill="var(--ink)"/>
          <rect x="8" y="10" width="14" height="10" fill="var(--card)"/>
          <path d="M8 10 L15 16 L22 10" fill="none" stroke="var(--ink)" stroke-width="1.3"/>
        </svg>
        <p class="contact-text">ned@nedhalvorsen.example.au</p>
      </li>
    </ul>

    <div class="rule rule-bottom"></div>
  </article>
</main>
</body>
</html>
```